Allied Health business card / Logo update.

Update/revitalise our logo and business cards. The logo needs to be suitable not only for business cards but stationary, website and clothing as well.

We have had the same hand logo for 16 years and have a strong brand name with this. One idea, however, was to base the idea around the similarities between the spine and bamboo. I will attach some images.

We are uncertain with colour. Initially, we thought earthy greens and greys/charcoal. However, we would also consider blue/charcoal combination.

I have attached our existing logo and this is our website. http://www.harbourleafspinal.com.au

Target Market(s)

General public
This is the only card

Industry/Entity Type

Health Care

Contact Information for Business Card

Harbourleaf Chiropractic Centre
27 Willowmere Road (Cnr Banfield St and Willowmere Rd) Port Macquarie
4/58 Thornbury St Wauchope
phone: 02 6571 4826
email: info@harbourleafspinal.com.au
web: harbourleafspinal.com.au

Marcus P. Helton
Cert. Rehab Therapist
Chiropractor
BSc(Syd)., MChirop(Mac)., MClinRehabNeuro(Flin)
MCAA, MAAFN, VEDA

Font styles to use
Serif
Sans Serif

Colors
acd037
85acd3
5c5c5c

Requirements
Must have
• Company name, Professional name with qualifications
• Contact details.

```html
<!DOCTYPE html>
<html lang="en">
<head>
<meta charset="utf-8">
<title>Harbourleaf Chiropractic Centre – Business Card</title>
<link rel="stylesheet" href="https://fonts.googleapis.com/css2?family=Open+Sans:wght@400;600&display=swap">
<style>
  :root {
    --page-bg: #2b2724;
    --card-dark: #0d0d0e;
    --card-blue: #3a90ca;
    --brand-blue: #3b92d0;
    --text-light: #f2f2f2;
    --text-muted: #c4c4c4;
    --rule: #3a4a5a;
  }
  * { box-sizing: border-box; margin: 0; padding: 0; }
  html, body { width: 1200px; height: 900px; overflow: hidden; }
  body {
    background: var(--page-bg);
    font-family: "Open Sans", Arial, sans-serif;
    position: relative;
  }
  .card {
    position: absolute;
    width: 540px;
    height: 310px;
    border-radius: 3px;
    box-shadow: 0 14px 30px rgba(0,0,0,.45);
  }

  /* Details side: dark */
  .card--details {
    left: 40px; top: 450px;
    background: var(--card-dark);
    color: var(--text-light);
  }
  .brand {
    position: absolute;
    left: 170px; top: 34px;
    display: flex; align-items: center; gap: 14px;
  }
  .brand__name {
    width: 200px;
    font-weight: 600;
    font-size: 26px;
    line-height: 1.04;
    color: var(--brand-blue);
  }
  .brand__dot {
    width: 20px; height: 20px; border-radius: 50%;
    background: var(--brand-blue);
  }
  .divider {
    position: absolute;
    left: 300px; top: 160px;
    width: 1px; height: 122px;
    background: var(--rule);
  }
  .person {
    position: absolute;
    right: 258px; top: 156px;
    width: 270px;
    text-align: right;
  }
  .person__name { color: var(--brand-blue); font-weight: 600; font-size: 16px; line-height: 22px; }
  .person__role { font-size: 12px; line-height: 16px; color: var(--text-light); }
  .person__quals { font-size: 10px; line-height: 14px; color: var(--text-muted); margin-bottom: 8px; }
  .person__address { font-size: 11px; line-height: 15px; color: var(--text-light); }
  .contacts {
    position: absolute;
    left: 316px; top: 162px;
    list-style: none;
    font-size: 12.5px;
    line-height: 1.6;
    color: var(--text-light);
  }
  .contacts li { display: flex; align-items: center; gap: 8px; }
  .contacts svg { width: 11px; height: 11px; fill: var(--brand-blue); flex: none; }

  /* Brand side: blue */
  .card--front {
    left: 620px; top: 130px;
    background: var(--card-blue);
    box-shadow: 0 4px 0 #1b1b1b, 0 8px 0 #161616, 0 12px 0 #121212, 0 22px 34px rgba(0,0,0,.5);
    display: flex; align-items: center; justify-content: center; gap: 16px;
  }
  .card--front .brand__name { color: #ffffff; width: 240px; font-size: 32px; }
  .card--front .brand__dot { background: #ffffff; width: 22px; height: 22px; }
</style>
</head>
<body>
  <section class="card card--details">
    <div class="brand">
      <p class="brand__name">Harbourleaf Chiropractic Centre</p>
      <span class="brand__dot"></span>
    </div>
    <span class="divider"></span>
    <div class="person">
      <p class="person__name">Marcus P. Helton</p>
      <p class="person__role">Chiropractor · Cert. Rehab Therapist</p>
      <p class="person__quals">BSc(Syd)., MChirop(Mac)., MClinRehabNeuro(Flin)<br>MCAA, MAAFN, VEDA</p>
      <p class="person__address">27 Willowmere Road, Port Macquarie<br>(Cnr Banfield St and Willowmere Rd)<br>4/58 Thornbury St, Wauchope</p>
    </div>
    <ul class="contacts">
      <li>
        <svg viewBox="0 0 24 24" aria-hidden="true"><path d="M6.6 10.8a15.5 15.5 0 0 0 6.6 6.6l2.2-2.2c.3-.3.7-.4 1-.2 1.1.4 2.3.6 3.6.6.6 0 1 .4 1 1V20c0 .6-.4 1-1 1A17 17 0 0 1 3 4c0-.6.4-1 1-1h3.5c.6 0 1 .4 1 1 0 1.3.2 2.5.6 3.6.1.3 0 .7-.2 1z"/></svg>
        02 6571 4826
      </li>
      <li>
        <svg viewBox="0 0 24 24" aria-hidden="true"><path d="M2 5h20v14H2zm2 2v.5l8 5 8-5V7z"/></svg>
        info@harbourleafspinal.com.au
      </li>
      <li>
        <svg viewBox="0 0 24 24" aria-hidden="true"><circle cx="12" cy="12" r="10"/></svg>
        harbourleafspinal.com.au
      </li>
    </ul>
  </section>

  <section class="card card--front">
    <p class="brand__name">Harbourleaf Chiropractic Centre</p>
    <span class="brand__dot"></span>
  </section>
</body>
</html>
```